Packaging for educational products for special needs kids - Drawer (pull-out) box

1. Modern, minimalist but attractive packaging for educational products for kids.
2. Approx size 24 x 15.5 x 2 cm.
3. Please refer to the sample packaging image for the kind of information that will be placed on the box. But the new designed box will be white.
4. The background on the sample images of a boy and a girl is used on all the cards so you can refer to this colour to be used in your designs.

Font styles to use
Sans Serif

Colors
87cfc6
cfeae6
f04a50
faa54b
fbee3d
abd036
00a990

```html
<!DOCTYPE html>
<html lang="en">
<head>
<meta charset="utf-8">
<title>Visual Schedules – Drawer Box Dieline</title>
<link href="https://fonts.googleapis.com/css2?family=Kaushan+Script&family=Poppins:wght@400;500;600;700&display=swap" rel="stylesheet">
<style>
  :root {
    --stage: #b5b5b5;
    --panel-top: #f4f4f4;
    --panel-mid: #ebebeb;
    --navy: #1f3583;
    --magenta: #e2187f;
    --coral: #f04a50;
    --orange: #faa54b;
    --teal: #12a48a;
    --aqua: #87cfc6;
    --aqua-light: #cfeae6;
    --ink: #1a1a1a;
    --white: #ffffff;
    --label: #d9d9d9;
  }
  * { box-sizing: border-box; margin: 0; padding: 0; }
  html, body { width: 1200px; height: 1200px; overflow: hidden; }
  body {
    background: var(--stage);
    font-family: "Poppins", sans-serif;
    position: relative;
  }
  .panel-label {
    position: absolute; top: 140px;
    font-family: "Poppins", sans-serif; font-weight: 600;
    font-size: 36px; color: var(--label);
  }
  .dieline {
    position: absolute; left: 38px; top: 200px;
    width: 1124px; height: 814px;
    display: flex;
  }
  .face {
    position: relative; height: 100%;
    background: linear-gradient(180deg, var(--panel-top), var(--panel-mid) 40%, var(--panel-top) 70%, var(--panel-mid));
  }
  .face--front { width: 525px; }
  .face--spine { width: 75px; }
  .face--back { width: 524px; }

  .brand {
    position: absolute; display: flex; align-items: center; gap: 10px;
    font-weight: 700; color: var(--navy); white-space: nowrap;
  }
  .brand__dot { width: 22px; height: 22px; border-radius: 50%; background: var(--coral); flex: none; }
  .face--front .brand { left: 0; right: 0; top: 88px; justify-content: center; font-size: 44px; }

  .title {
    font-family: "Kaushan Script", cursive; color: var(--navy); white-space: nowrap;
  }
  .subtitle { color: var(--magenta); font-weight: 500; white-space: nowrap; letter-spacing: 0.5px; }
  .face--front .title { position: absolute; left: 0; right: 0; top: 182px; text-align: center; font-size: 56px; line-height: 1; }
  .face--front .subtitle { position: absolute; left: 0; right: 0; top: 262px; text-align: center; font-size: 31px; line-height: 1; }

  .scene-card {
    position: absolute; top: 326px; height: 204px; width: 231px;
    border-radius: 12px; border: 1.5px solid #7a8a99;
    background: linear-gradient(180deg, var(--aqua-light) 0%, var(--aqua-light) 45%, #bcd9ef 70%, #a9cbe6 100%);
  }
  .scene-card--boy { left: 21px; }
  .scene-card--girl { left: 272px; }

  .tag {
    position: absolute; left: 130px; top: 559px; width: 263px; height: 38px;
    border-radius: 19px; background: var(--coral); color: var(--white);
    font-size: 22px; font-weight: 500; letter-spacing: -0.5px;
    display: flex; align-items: center; justify-content: center;
  }

  .handling { position: absolute; display: flex; flex-direction: column; align-items: center; gap: 6px; }
  .face--front .handling { left: 0; right: 0; top: 670px; }
  .handling__title { font-size: 15px; font-weight: 600; color: var(--ink); letter-spacing: 0.2px; }
  .handling__icons { display: flex; gap: 8px; }
  .handling__icon { width: 36px; display: flex; flex-direction: column; align-items: center; }
  .handling__icon svg { width: 34px; height: 30px; display: block; }
  .handling__icon span { font-size: 3.5px; font-weight: 700; color: var(--ink); white-space: nowrap; margin-top: 1px; }

  .band { position: absolute; left: 0; right: 0; bottom: 0; height: 55px; background: var(--teal); }

  .face--spine {
    background: linear-gradient(90deg, var(--white) 0 10px, transparent 10px),
                linear-gradient(180deg, #f49a3e 0%, var(--orange) 55%, #fcd9b2 85%, var(--white) 100%);
  }
  .spine-stack {
    position: absolute; left: 50%; top: 24px;
    transform-origin: 0 0; transform: rotate(90deg) translateY(-50%);
    display: flex; align-items: baseline; white-space: nowrap;
  }
  .spine-stack .brand { position: static; font-size: 22px; gap: 6px; }
  .spine-stack .brand__dot { width: 12px; height: 12px; }
  .spine-stack .title { font-size: 40px; margin-left: 120px; }
  .spine-stack .subtitle { font-size: 20px; margin-left: 8px; }

  .label-window {
    position: absolute; left: 61px; top: 96px; width: 394px; height: 648px;
    background: var(--white); border-radius: 18px;
  }
  .label-window .handling { left: 0; right: 0; top: 32px; transform: rotate(180deg); flex-direction: column-reverse; }
</style>
</head>
<body>
  <div class="panel-label" style="left:268px">Front</div>
  <div class="panel-label" style="left:797px">Back</div>

  <div class="dieline">
    <section class="face face--front">
      <div class="brand"><span class="brand__dot"></span>Bright Steps</div>
      <h1 class="title">Visual Schedules</h1>
      <p class="subtitle">HELPERS AT HOME</p>

      <div class="scene-card scene-card--boy" role="img" aria-label="Illustration of a boy stretching in bed beside an alarm clock"></div>
      <div class="scene-card scene-card--girl" role="img" aria-label="Illustration of a girl stretching in bed beside an alarm clock"></div>

      <div class="tag">PACKAGE FOR KIDS</div>

      <div class="handling">
        <p class="handling__title">PLEASE THIS SIDE UP</p>
        <div class="handling__icons">
          <div class="handling__icon">
            <svg viewBox="0 0 34 30"><rect x="1" y="1" width="32" height="28" fill="none" stroke="#1a1a1a" stroke-width="1.5"/><path d="M12 24V8M8 12l4-5 4 5M22 24V8M18 12l4-5 4 5" stroke="#1a1a1a" stroke-width="2.5" fill="none"/><path d="M7 26h20" stroke="#1a1a1a" stroke-width="1.5"/></svg>
            <span>THIS SIDE UP</span>
          </div>
          <div class="handling__icon">
            <svg viewBox="0 0 34 30"><rect x="1" y="1" width="32" height="28" fill="none" stroke="#1a1a1a" stroke-width="1.5"/><rect x="12" y="7" width="10" height="9" fill="#1a1a1a"/><path d="M7 13l5 8h10l5-8" stroke="#1a1a1a" stroke-width="2.5" fill="none"/></svg>
            <span>HANDLE WITH CARE</span>
          </div>
          <div class="handling__icon">
            <svg viewBox="0 0 34 30"><rect x="1" y="1" width="32" height="28" fill="none" stroke="#1a1a1a" stroke-width="1.5"/><path d="M10 5h14l-2 9a5 5 0 0 1-10 0z" fill="#1a1a1a"/><path d="M17 19v6M12 25h10" stroke="#1a1a1a" stroke-width="2"/></svg>
            <span>FRAGILE</span>
          </div>
          <div class="handling__icon">
            <svg viewBox="0 0 34 30"><rect x="1" y="1" width="32" height="28" fill="none" stroke="#1a1a1a" stroke-width="1.5"/><path d="M12 6h10l-6 15" stroke="#1a1a1a" stroke-width="2.5" fill="none"/><path d="M7 24h20M7 27h20" stroke="#1a1a1a" stroke-width="1.5"/></svg>
            <span>MAX STACK</span>
          </div>
        </div>
      </div>

      <div class="band"></div>
    </section>

    <section class="face face--spine">
      <div class="spine-stack">
        <div class="brand"><span class="brand__dot"></span>Bright Steps</div>
        <span class="title">Visual Schedules</span>
        <span class="subtitle">HELPERS AT HOME</span>
      </div>
    </section>

    <section class="face face--back">
      <div class="label-window">
        <div class="handling">
          <p class="handling__title">PLEASE THIS SIDE UP</p>
          <div class="handling__icons">
            <div class="handling__icon">
              <svg viewBox="0 0 34 30"><rect x="1" y="1" width="32" height="28" fill="none" stroke="#1a1a1a" stroke-width="1.5"/><path d="M12 24V8M8 12l4-5 4 5M22 24V8M18 12l4-5 4 5" stroke="#1a1a1a" stroke-width="2.5" fill="none"/><path d="M7 26h20" stroke="#1a1a1a" stroke-width="1.5"/></svg>
              <span>THIS SIDE UP</span>
            </div>
            <div class="handling__icon">
              <svg viewBox="0 0 34 30"><rect x="1" y="1" width="32" height="28" fill="none" stroke="#1a1a1a" stroke-width="1.5"/><rect x="12" y="7" width="10" height="9" fill="#1a1a1a"/><path d="M7 13l5 8h10l5-8" stroke="#1a1a1a" stroke-width="2.5" fill="none"/></svg>
              <span>HANDLE WITH CARE</span>
            </div>
            <div class="handling__icon">
              <svg viewBox="0 0 34 30"><rect x="1" y="1" width="32" height="28" fill="none" stroke="#1a1a1a" stroke-width="1.5"/><path d="M10 5h14l-2 9a5 5 0 0 1-10 0z" fill="#1a1a1a"/><path d="M17 19v6M12 25h10" stroke="#1a1a1a" stroke-width="2"/></svg>
              <span>FRAGILE</span>
            </div>
            <div class="handling__icon">
              <svg viewBox="0 0 34 30"><rect x="1" y="1" width="32" height="28" fill="none" stroke="#1a1a1a" stroke-width="1.5"/><path d="M12 6h10l-6 15" stroke="#1a1a1a" stroke-width="2.5" fill="none"/><path d="M7 24h20M7 27h20" stroke="#1a1a1a" stroke-width="1.5"/></svg>
              <span>MAX STACK</span>
            </div>
          </div>
        </div>
      </div>
    </section>
  </div>
</body>
</html>
```